Somebody commencing retirement at age 67 and wanting a card to introduce myself

Something that depicts the activities I intend to pursue in retirement: Travel, Golf (both in Australia and internationally), wining (red) and dining and generally leading a decadent lifestyle with my wife (or by myself as appropriate).

I offer no services, but intend to have a decadent, relaxing
retirement, playing golf, drinking red wine and dining at good
restaurants!

The card needs to have a suitably designed logo that reflects the
foregoing.

Requirements
Must have
• On the front of the card, my photograph (attached and cropped as
• appropriate), my name (Carl Brimstead), my mobile phone number (+61 417
• 532 148), my email address (carl@brimstead.example.au) and my residential
• address (41 Kestrel Lane, Marlowe Heights, Western Australia 6031,
• Australia).
• The rear of the card should have my postal address (Carl Brimstead
• Post Office Box 518 Dunmore Western Australia 6947, Australia.)._

```html
<!DOCTYPE html>
<html lang="en">
<head>
<meta charset="utf-8">
<title>Carl Brimstead — Business Card</title>
<link rel="stylesheet" href="https://fonts.googleapis.com/css2?family=Lato:wght@400;700&display=swap">
<style>
  :root {
    --backdrop: #141414;
    --card: #1d1d1d;
    --card-sheen: #2b2b2b;
    --ink: #f4f4f4;
    --ink-soft: #d9d9d9;
  }
  * { margin: 0; padding: 0; box-sizing: border-box; }
  html, body {
    width: 1200px;
    height: 900px;
    overflow: hidden;
    background: var(--backdrop);
    font-family: "Lato", Arial, sans-serif;
    color: var(--ink);
  }
  .canvas {
    width: 1200px;
    height: 900px;
    display: flex;
    flex-direction: column;
    align-items: center;
    justify-content: center;
    gap: 36px;
  }
  .card {
    width: 720px;
    height: 400px;
    background: linear-gradient(120deg, var(--card) 0%, var(--card) 55%, var(--card-sheen) 85%, var(--card) 100%);
    position: relative;
  }

  /* Back: brand and postal address */
  .card--back .brand {
    position: absolute;
    top: 112px;
    left: 0;
    right: 0;
    display: flex;
    align-items: center;
    justify-content: center;
    gap: 22px;
  }
  .brand__ring {
    width: 96px;
    height: 96px;
    border: 2px solid var(--ink);
    border-radius: 50%;
  }
  .brand__name {
    font-size: 26px;
    font-weight: 400;
    letter-spacing: 4px;
    text-transform: uppercase;
    color: var(--ink);
  }
  .card--back .addresses {
    position: absolute;
    top: 268px;
    left: 0;
    right: 0;
    text-align: center;
    font-size: 17px;
    line-height: 1.5;
    color: var(--ink-soft);
  }

  /* Front: name and contact */
  .card--front .contact-block {
    position: absolute;
    top: 168px;
    left: 0;
    right: 0;
    display: flex;
    justify-content: center;
    align-items: center;
    gap: 28px;
  }
  .identity { text-align: right; }
  .identity__name {
    font-size: 21px;
    font-weight: 700;
    letter-spacing: 0.5px;
    text-transform: uppercase;
  }
  .identity__role {
    font-size: 17px;
    color: var(--ink-soft);
    margin-top: 2px;
  }
  .divider {
    width: 1.5px;
    height: 44px;
    background: var(--ink);
  }
  .contact-list { list-style: none; font-size: 18px; line-height: 1.45; }
  .contact-list li { display: flex; align-items: center; gap: 10px; }
  .contact-list svg { width: 14px; height: 14px; flex: none; }
</style>
</head>
<body>
  <main class="canvas">
    <section class="card card--back">
      <div class="brand">
        <span class="brand__ring"></span>
        <span class="brand__name">Carl Brimstead</span>
      </div>
      <address class="addresses" style="font-style: normal;">
        Box 518 Dunmore Western Australia 6947, Australia.<br>
        41 Kestrel Lane, Marlowe Heights, Western Australia 6031, Australia
      </address>
    </section>

    <section class="card card--front">
      <div class="contact-block">
        <div class="identity">
          <p class="identity__name">Carl Brimstead</p>
          <p class="identity__role">Photograph</p>
        </div>
        <span class="divider"></span>
        <ul class="contact-list">
          <li>
            <svg viewBox="0 0 16 16" aria-hidden="true"><path d="M4 1.5l2 3-1.3 1.3c.8 1.8 2.3 3.3 4.1 4.1L10.1 8.6l3 2-1 2.6C7 13 3 9 2.6 3.4z" fill="none" stroke="#f4f4f4" stroke-width="1.4" stroke-linejoin="round"/></svg>
            <span>(+61 417 - 532 148)</span>
          </li>
          <li>
            <svg viewBox="0 0 16 16" aria-hidden="true"><rect x="1.5" y="3.5" width="13" height="9" fill="none" stroke="#f4f4f4" stroke-width="1.4"/><path d="M1.5 3.5L8 9l6.5-5.5" fill="none" stroke="#f4f4f4" stroke-width="1.4"/></svg>
            <span>carl@brimstead.example.au</span>
          </li>
        </ul>
      </div>
    </section>
  </main>
</body>
</html>
```